Rivolex.com Trucking Company Website

Need a website designed (no content) for a trucking company, specializing in trucking of ocean containers (intermodal Trucking). Heavy emphasis on technology, using latest technology, providing unabated visibility and realtime information.
clean minimalist industrial website
example:
https://www.bramtiq.com/

Target Market(s)

Professional Business Consumer corporate and small business

Industry/Entity Type

Trucking Company

Number of Pages Required

5+ page

Requirements
Must have
• Industrial Design, simple informative, for a busy professional to view and get the necessary information with out the distractions.
• Blog Page
• Client Log-In on the front page
• Technology page - showing our intensive investments in technology
Nice to have
• If ANY images included, MUST be USA related. Example if include an image of a truck, ensure its a USA model. Do the research.
• included our business card for sample of Logo
• Doesnt not have to be the same color schemes.
Should not have
• moving images

```html
<!DOCTYPE html>
<html lang="en">
<head>
<meta charset="utf-8">
<title>Rivolex Consulting — Intermodal Trucking</title>
<link rel="stylesheet" href="https://fonts.googleapis.com/css2?family=Open+Sans:ital,wght@0,400;0,600;0,700;0,800;1,400&display=swap">
<style>
:root{
  --ink:#0b0b0b;
  --slate:#464c52;
  --grey:#8a8a8a;
  --light:#f2f2f2;
  --rule:#bdbdbd;
  --white:#ffffff;
  --green:#1aa34a;
  --footer:#1d1c1b;
  --link:#8aa6c4;
}
*{box-sizing:border-box;margin:0;padding:0}
html,body{width:1200px;height:2228px;overflow:hidden;background:var(--white)}
body{position:relative;font-family:"Open Sans",Arial,sans-serif;color:var(--ink)}
.abs{position:absolute}

/* utility bar */
.utility-bar{left:0;top:0;width:1200px;height:18px;background:var(--ink)}
.utility-bar a{position:absolute;top:2px;font-size:10px;color:var(--white);text-decoration:none;letter-spacing:.3px}

/* header */
.site-header{left:0;top:18px;width:1200px;height:74px;border-bottom:1px solid var(--rule)}
.brand{position:absolute;left:64px;top:10px;color:var(--slate);font-weight:700;line-height:1}
.brand .name{font-size:34px;letter-spacing:1px}
.brand .sub{font-size:12px;letter-spacing:4.6px;margin-top:2px}
.main-nav{position:absolute;right:40px;top:24px;display:flex;gap:22px}
.main-nav a{font-size:15px;color:var(--ink);text-decoration:none;letter-spacing:.6px}

/* hero */
.hero{left:0;top:92px;width:1200px;height:495px}
.hero h1{position:absolute;left:108px;top:140px;font-size:38px;line-height:44px;font-weight:800;color:var(--slate);letter-spacing:2.4px}
.hero p{position:absolute;left:108px;top:270px;width:380px;font-size:15px;line-height:17px;color:var(--ink);letter-spacing:.4px}
.btn{position:absolute;display:flex;align-items:center;justify-content:center;font-size:13px;letter-spacing:1px;text-decoration:none;border-radius:7px}
.btn-outline{border:1.5px solid var(--ink);color:var(--ink);background:var(--white)}
.btn-solid{background:var(--ink);color:var(--white)}
.hero-photo{position:absolute;left:497px;top:64px;width:703px;height:371px;background:linear-gradient(135deg,#f4f4f4 0%,#d9d9d9 45%,#7a7a7a 75%,#4a4a4a 100%);clip-path:polygon(0 55%,20% 35%,45% 12%,100% 0,100% 100%,8% 100%)}
.hero-arrow{position:absolute}

/* partner band */
.partners{left:0;top:587px;width:1200px;height:136px;background:var(--light)}
.badge{position:absolute}

/* login */
.section-title{position:absolute;font-size:30px;font-weight:600;letter-spacing:.6px;text-align:center}
.divider{left:621px;top:787px;width:1px;height:285px;background:#555}
.field{position:absolute;left:160px;width:309px;height:33px;border:1.5px solid var(--ink);display:flex;align-items:center}
.field .icon{width:28px;height:100%;background:var(--ink);display:flex;align-items:center;justify-content:center}
.field span{padding-left:12px;font-size:13px;font-style:italic;color:var(--grey);letter-spacing:.6px}
.forgot{left:169px;top:977px;font-size:11px;font-style:italic;color:var(--link);text-decoration:underline}
.perk{position:absolute;left:716px;display:flex;gap:18px;width:320px}
.perk p{font-size:13px;line-height:15px}

/* technology */
.eyebrow{left:0;width:1200px;top:1166px;text-align:center;font-size:14px;color:var(--slate);letter-spacing:1px}
.provide{left:0;width:1200px;top:1180px;text-align:center;font-size:44px;font-weight:700;letter-spacing:.6px}
.tech-photo{left:0;top:1336px;width:594px;height:491px;background:linear-gradient(120deg,#cfcfcf 0%,#f4f4f4 40%,#a9a9a9 70%,#ffffff 100%);clip-path:polygon(0 4%,30% 0,55% 12%,100% 70%,96% 92%,0 100%)}
.feature{position:absolute;left:711px;width:300px;text-align:center}
.feature h3{font-size:18px;font-weight:600;letter-spacing:2px;color:var(--ink)}
.feature p{font-size:12px;line-height:15px;color:var(--grey);letter-spacing:.6px;margin-top:4px}

/* footer */
.site-footer{left:0;top:1954px;width:1200px;height:274px;background:var(--footer);color:var(--white)}
.site-footer .brand{left:85px;top:40px;color:var(--white)}
.contact{position:absolute;left:88px;display:flex;align-items:center;gap:18px;font-size:12px}
.contact svg{width:14px;height:14px}
.footer-heading{position:absolute;font-size:18px;font-weight:700;letter-spacing:.4px}
.footer-rule{position:absolute;height:1px;background:#777}
.about-copy{position:absolute;left:396px;top:2066px;width:345px;font-size:12px;line-height:26px;color:#dcdcdc}
.sitemap a{position:absolute;font-size:12px;color:var(--white);text-decoration:none}
.copyright{left:40px;top:2195px;font-size:12px;color:var(--white)}
</style>
</head>
<body>

<div class="abs utility-bar">
  <a href="#" style="left:969px">MEMBER LOGIN</a>
  <a href="#" style="left:1064px">CORPORATE LOGIN</a>
</div>

<header class="abs site-header">
  <div class="brand"><div class="name">RIVOLEX</div><div class="sub">CONSULTING</div></div>
  <nav class="main-nav">
    <a href="#">Home</a><a href="#">About us</a><a href="#">Technology</a><a href="#">Blog</a><a href="#">Contact us</a>
  </nav>
</header>

<section class="abs hero">
  <svg class="hero-arrow" style="left:18px;top:222px" width="22" height="28" viewBox="0 0 22 28"><path d="M17 3 L6 14 L17 25" fill="none" stroke="#555" stroke-width="5"/></svg>
  <h1>WE MAKE SHIPPING<br>BIG STUFF EASY</h1>
  <p>Join the millions getting bargain deals on shipping cars, furniture, freight, and more...</p>
  <a href="#" class="btn btn-outline" style="left:105px;top:343px;width:128px;height:36px">LEARN MORE</a>
  <a href="#" class="btn btn-solid" style="left:239px;top:343px;width:128px;height:36px">LOGIN</a>
  <div class="hero-photo" role="img" aria-label="Photo of a white US semi truck hauling an ocean shipping container"></div>
</section>

<section class="abs partners" aria-label="Partner manufacturers">
  <svg class="badge" style="left:146px;top:25px" width="94" height="94" viewBox="0 0 94 94"><circle cx="47" cy="47" r="42" fill="#c9c9c9" stroke="#8c8c8c" stroke-width="4"/></svg>
  <svg class="badge" style="left:374px;top:56px" width="188" height="32" viewBox="0 0 188 32"><rect width="188" height="32" fill="#7a7a7a"/></svg>
  <svg class="badge" style="left:695px;top:28px" width="78" height="80" viewBox="0 0 78 80"><rect x="16" y="16" width="46" height="46" transform="rotate(45 39 39)" fill="#9a9a9a" stroke="#555" stroke-width="3"/></svg>
  <svg class="badge" style="left:908px;top:47px" width="146" height="60" viewBox="0 0 146 60"><ellipse cx="73" cy="30" rx="71" ry="28" fill="#444" stroke="#999" stroke-width="3"/></svg>
</section>

<h2 class="section-title" style="left:169px;top:794px;width:300px">USER LOGIN</h2>
<div class="field" style="top:894px"><div class="icon"><svg width="12" height="14" viewBox="0 0 12 14"><circle cx="6" cy="4" r="3.5" fill="#fff"/><path d="M0 14 Q6 5 12 14Z" fill="#fff"/></svg></div><span>Username/E-mail Address</span></div>
<div class="field" style="top:941px"><div class="icon"><svg width="12" height="14" viewBox="0 0 12 14"><path d="M3 6 V4 a3 3 0 0 1 6 0 V6" fill="none" stroke="#fff" stroke-width="1.6"/><rect x="1" y="6" width="10" height="8" fill="#fff"/></svg></div><span>Login Password</span></div>
<a href="#" class="abs forgot">forgot your password?</a>
<a href="#" class="btn btn-solid" style="left:379px;top:1004px;width:90px;height:36px;border-radius:18px;font-size:12px">LOGIN</a>

<div class="abs divider"></div>

<h2 class="section-title" style="left:720px;top:794px;width:300px">BY SIGNING UP</h2>
<div class="perk" style="top:865px"><svg width="15" height="12" viewBox="0 0 15 12"><path d="M1 6 L5.5 10 L14 1.5" fill="none" stroke="var(--green)" stroke-width="2.6"/></svg><p>Lorem ipsum dolor sit amet, consectetur adipiscing elit</p></div>
<div class="perk" style="top:914px"><svg width="15" height="12" viewBox="0 0 15 12"><path d="M1 6 L5.5 10 L14 1.5" fill="none" stroke="var(--green)" stroke-width="2.6"/></svg><p>Lorem ipsum dolor sit amet, consectetur adipiscing elit</p></div>
<div class="perk" style="top:964px"><svg width="15" height="12" viewBox="0 0 15 12"><path d="M1 6 L5.5 10 L14 1.5" fill="none" stroke="var(--green)" stroke-width="2.6"/></svg><p>Lorem ipsum dolor sit amet, consectetur adipiscing elit</p></div>
<a href="#" class="btn btn-solid" style="left:803px;top:1019px;width:134px;height:50px;border-radius:25px;font-size:12px">SIGN UP</a>

<p class="abs eyebrow">State of the art technology</p>
<h2 class="abs provide">WE PROVIDE</h2>

<div class="abs tech-photo" role="img" aria-label="Photo of a white conventional US semi truck with a box trailer"></div>

<div class="feature" style="top:1346px">
  <svg width="84" height="66" viewBox="0 0 84 66"><path d="M4 6 H50 V50 H4Z M50 20 H68 L80 36 V50 H50" fill="none" stroke="#111" stroke-width="3" stroke-linejoin="round"/><path d="M56 24 H66 L74 36 H56Z" fill="none" stroke="#111" stroke-width="2.5"/><circle cx="18" cy="54" r="7" fill="#fff" stroke="#111" stroke-width="3"/><circle cx="64" cy="54" r="7" fill="#fff" stroke="#111" stroke-width="3"/></svg>
  <h3>LATEST TECHNOLOGY</h3>
  <p>Lorem ipsum dolor sit amet,<br>consectetur adipiscing elit</p>
</div>
<div class="feature" style="top:1532px">
  <svg width="92" height="58" viewBox="0 0 92 58"><path d="M3 29 Q46 -12 89 29 Q46 70 3 29Z" fill="none" stroke="#111" stroke-width="3"/><circle cx="46" cy="29" r="13" fill="none" stroke="#111" stroke-width="3"/><circle cx="46" cy="29" r="5" fill="#111"/></svg>
  <h3>UNABATED VISIBILITY</h3>
  <p>Lorem ipsum dolor sit amet,<br>consectetur adipiscing elit</p>
</div>
<div class="feature" style="top:1718px">
  <svg width="80" height="80" viewBox="0 0 80 80"><circle cx="48" cy="30" r="24" fill="none" stroke="#111" stroke-width="2.5" stroke-dasharray="120 20"/><text x="48" y="38" text-anchor="middle" font-family="Open Sans, Arial, sans-serif" font-size="20" font-weight="600">24</text><path d="M8 28 C4 40 22 70 44 72 L50 64 L40 54 L33 58 C26 52 22 46 20 38 L26 32 L18 20Z" fill="none" stroke="#111" stroke-width="2.5" stroke-linejoin="round"/></svg>
  <h3>REALTIME INFORMATION</h3>
  <p>Lorem ipsum dolor sit amet,<br>consectetur adipiscing elit</p>
</div>

<footer class="abs site-footer">
  <div class="brand"><div class="name">RIVOLEX</div><div class="sub">CONSULTING</div></div>
</footer>

<div class="contact" style="top:2060px;color:#fff"><svg viewBox="0 0 14 14"><path d="M7 0 a5 5 0 0 1 5 5 C12 9 7 14 7 14 C7 14 2 9 2 5 a5 5 0 0 1 5-5Z" fill="#fff"/><circle cx="7" cy="5" r="2" fill="#1d1c1b"/></svg>48 Harbor Line Road, CA 90812</div>
<div class="contact" style="top:2086px;color:#fff"><svg viewBox="0 0 14 14"><rect x="1" y="3" width="12" height="9" fill="#fff"/><path d="M1 3 L7 8 L13 3" fill="none" stroke="#1d1c1b" stroke-width="1.2"/></svg>info@rivolexconsulting.com</div>
<div class="contact" style="top:2112px;color:#fff"><svg viewBox="0 0 14 14"><circle cx="7" cy="7" r="5.5" fill="none" stroke="#fff" stroke-width="1.6"/><path d="M7 4 V7 H9.5" fill="none" stroke="#fff" stroke-width="1.4"/></svg>Monday through Sunday, 24/7</div>
<div class="contact" style="top:2138px;color:#fff"><svg viewBox="0 0 14 14"><path d="M2 2 L5 1.5 L6.5 5 L5 6.5 C6 8.5 7 9.5 8.5 10 L10 8.5 L13 10 L12.5 13 C6 13 1 8 2 2Z" fill="#fff"/></svg>Call us now: (555) 0148-2290</div>

<h4 class="footer-heading" style="left:396px;top:2010px;color:#fff">ABOUT US</h4>
<div class="footer-rule" style="left:396px;top:2045px;width:336px"></div>
<p class="about-copy">Lorem ipsum dolor sit amet, consectetur adipisicing elit, sed do eiusmod tempor incididunt ut labore et dolore magna aliqua. Ut enim ad minim veniam, quis nostrud exercitation ullamco laboris nisi ut aliquip ex ea commodo consequat.</p>

<h4 class="footer-heading" style="left:803px;top:2010px;color:#fff">SITE MAP</h4>
<div class="footer-rule" style="left:803px;top:2045px;width:336px"></div>
<nav class="sitemap">
  <a href="#" style="left:803px;top:2063px">Home</a>
  <a href="#" style="left:941px;top:2063px">Blog</a>
  <a href="#" style="left:803px;top:2099px">About us</a>
  <a href="#" style="left:941px;top:2099px">Contact us</a>
  <a href="#" style="left:803px;top:2135px">Technology</a>
  <a href="#" style="left:943px;top:2135px">Privacy/Policy</a>
  <a href="#" style="left:803px;top:2170px">Services</a>
  <a href="#" style="left:943px;top:2170px">FAQ</a>
</nav>

<p class="abs copyright">© 2017 Rivolex Consulting, Inc. All Rights Reserved</p>

</body>
</html>
```